Exciting Personal Development Book Cover: FIND ZEN NOW!

Design a Book Cover for my personal development book.
Title: Find Zen Now!
Author: Marcus Telly
Tagline: A real-life solution to get unstuck and break free

My picture must make up the front cover as I need to build my brand and people should recognise me on book shelves. Bold and catchy. How you do it is up to you. There must be space for a short testimonial from a famous person who is currently reading my book. I uploaded a sample of what I made in Photoshop but I don't have design skills.

I've added a PDF of my book so you can read the chapter index and introduction to get a sense of the content.

Target Market(s)

Personal Development Self-Help Market

Industry/Entity Type

Personal Development

Font styles to use
Serif
Sans Serif

Requirements
Must have
• My picture as hero image on cover.
Nice to have
• Must have Title, Tagline and my author name. If possible ZEN stands for 'Zeal, Energy & Nerve' If there is a way to fit this somewhere great. If it's too much then it can go somewhere on the back.

```html
<!DOCTYPE html>
<html lang="en">
<head>
<meta charset="utf-8">
<title>Find Zen Now! — Marcus Telly</title>
<link rel="stylesheet" href="https://fonts.googleapis.com/css2?family=Oswald:wght@600;700&family=Roboto+Condensed:ital,wght@0,700;1,400&display=swap">
<style>
  :root {
    --sky: #a4cdef;
    --paper: #ffffff;
    --ink: #111111;
    --muted: #4a4a4a;
    --author: #8a2a17;
    --portrait-light: #eef0f2;
    --portrait-mid: #c8ccd1;
    --portrait-dark: #7f8a96;
  }
  html, body {
    margin: 0;
    padding: 0;
    width: 778px;
    height: 1200px;
    overflow: hidden;
    background: var(--paper);
  }
  .cover {
    position: relative;
    width: 778px;
    height: 1200px;
    overflow: hidden;
    background: var(--paper);
  }
  .cover__backdrop,
  .cover__portrait {
    position: absolute;
    left: 0;
    top: 0;
  }
  .cover__title {
    position: absolute;
    left: 36px;
    top: 8px;
    margin: 0;
    font-family: "Oswald", "Arial Narrow", sans-serif;
    font-weight: 700;
    font-size: 190px;
    line-height: 200px;
    letter-spacing: 2px;
    color: var(--paper);
    text-transform: uppercase;
  }
  .cover__title-line { display: block; }
  .cover__title-bang { color: var(--ink); }
  .cover__tagline {
    position: absolute;
    left: 36px;
    top: 695px;
    width: 250px;
    margin: 0;
    font-family: "Roboto Condensed", "Arial Narrow", sans-serif;
    font-weight: 700;
    font-size: 36px;
    line-height: 42px;
    color: var(--ink);
  }
  .cover__testimonial {
    position: absolute;
    left: 36px;
    top: 895px;
    width: 270px;
    margin: 0;
    font-family: "Roboto Condensed", "Arial Narrow", sans-serif;
    font-style: italic;
    font-weight: 400;
    font-size: 20px;
    line-height: 26px;
    color: var(--muted);
  }
  .cover__testimonial-source {
    display: block;
    font-style: normal;
    font-weight: 700;
    color: var(--ink);
  }
  .cover__author {
    position: absolute;
    left: 36px;
    top: 1015px;
    margin: 0;
    font-family: "Oswald", "Arial Narrow", sans-serif;
    font-weight: 600;
    font-size: 80px;
    line-height: 88px;
    letter-spacing: 2px;
    color: var(--author);
    text-transform: uppercase;
  }
  .cover__author span { display: block; }
</style>
</head>
<body>
  <main class="cover">
    <svg class="cover__backdrop" width="778" height="1200" viewBox="0 0 778 1200" aria-hidden="true">
      <polygon points="0,0 778,0 778,560 0,690" fill="var(--sky)"/>
    </svg>

    <svg class="cover__portrait" width="778" height="1200" viewBox="0 0 778 1200" role="img" aria-label="Portrait of author Marcus Telly in a white shirt, smiling, tattooed forearms crossed at the chest">
      <defs>
        <linearGradient id="portrait-tone" x1="0" y1="0" x2="0" y2="1">
          <stop offset="0" stop-color="var(--portrait-mid)"/>
          <stop offset="0.4" stop-color="var(--portrait-light)"/>
          <stop offset="0.75" stop-color="var(--portrait-mid)"/>
          <stop offset="1" stop-color="var(--portrait-dark)"/>
        </linearGradient>
      </defs>
      <path d="M330 1200 L330 770 Q330 640 450 600 L470 300 Q480 175 600 170 Q720 170 740 300 L778 330 L778 1200 Z" fill="url(#portrait-tone)"/>
    </svg>

    <h1 class="cover__title">
      <span class="cover__title-line">Find</span>
      <span class="cover__title-line">Zen</span>
      <span class="cover__title-line">Now<span class="cover__title-bang">!</span></span>
    </h1>

    <p class="cover__tagline">A REAL-LIFE solution to get unstuck and break free</p>

    <p class="cover__testimonial">“A short line of praise from a well-known reader goes here.”
      <span class="cover__testimonial-source">— Jordan Vale</span>
    </p>

    <p class="cover__author">
      <span>Marcus</span>
      <span>Telly</span>
    </p>
  </main>
</body>
</html>
```